BRIXLEY ELECTRICAL

all black background with silver and lime writing, fonts i like are gothic style but am open to ideas, will need a picture logo aswell as im putting this on my van.i am a electrical contractor starting up my own electrical business. underneath brixley electrical heading on card we could put" professiona cost effective soloutions to all your electrical needs".{ or something of that nature }.on aback of card on top half list servises provided, real estate and commercial maintenance, new home and renovation rewires and upgrades, split system air conditioning, floor heat, tv phone data, smoke detoctors, lighting systems , builders welcome, , and also a thankyou for your business.

Industry/Entity Type

Real Estate

Contact Information for Business Card

GAVIN PRESTWORTH
brixleyelectrical@quillnet.com.au
0417352940
lic no 81926
ac lic no l593721
abn 37216405813

```html
<!DOCTYPE html>
<html lang="en">
<head>
<meta charset="utf-8">
<title>Brixley Electrical – Business Card</title>
<link rel="stylesheet" href="https://fonts.googleapis.com/css2?family=Arimo:wght@400;700&family=Pinyon+Script&display=swap">
<style>
  :root {
    --page: #e6e4e0;
    --card-black: #0b0b0b;
    --card-white: #ffffff;
    --silver: #d8d8d8;
    --lime: #39e41a;
    --rule: #bdbdbd;
  }
  * { margin: 0; padding: 0; box-sizing: border-box; }
  html, body {
    width: 1200px; height: 1200px; overflow: hidden;
    background: var(--page);
    font-family: "Arimo", Arial, sans-serif;
  }
  .sheet {
    width: 1200px; height: 1200px;
    display: flex; flex-direction: column; align-items: center; justify-content: center;
    gap: 52px;
  }
  .card {
    width: 900px; height: 514px;
    position: relative; overflow: hidden;
    box-shadow: 0 10px 28px rgba(0,0,0,.25);
  }

  /* Front */
  .card-front { background: var(--card-black); }
  .brand {
    position: absolute; left: 70px; top: 70px;
    display: flex; align-items: center; gap: 18px;
  }
  .brand-mark {
    width: 34px; height: 34px; border-radius: 50%;
    background: var(--lime);
  }
  .brand-name {
    color: var(--silver);
    font-size: 34px; font-weight: 700; letter-spacing: 6px;
  }
  .brand-tagline {
    position: absolute; left: 70px; top: 124px;
    color: var(--lime);
    font-size: 18px; letter-spacing: 2px;
  }
  .holder-name {
    position: absolute; left: 70px; top: 250px;
    color: var(--silver);
    font-size: 40px; font-weight: 400;
    letter-spacing: 7px;
  }
  .name-rule {
    position: absolute; left: 70px; right: 60px; top: 312px;
    height: 2px; background: var(--rule);
  }
  .contact-list {
    position: absolute; right: 60px; top: 336px;
    list-style: none; text-align: left;
    color: var(--lime);
    font-size: 20px; line-height: 32px; letter-spacing: 1.5px;
  }

  /* Back */
  .card-back { background: var(--card-black); }
  .services-band {
    position: absolute; left: 0; right: 0; top: 0; height: 230px;
    background: var(--card-white);
    text-align: center;
    padding: 30px 36px 0;
    color: var(--lime);
  }
  .services-title {
    font-size: 30px; font-weight: 700; letter-spacing: 2px;
    margin-bottom: 8px;
  }
  .services-list {
    font-size: 22px; line-height: 30px; letter-spacing: 3px;
  }
  .tagline {
    position: absolute; left: 0; right: 0; top: 262px;
    text-align: center;
    color: var(--silver);
    font-size: 22px; font-weight: 700; letter-spacing: 6px;
    line-height: 40px;
  }
  .thanks {
    position: absolute; left: 0; right: 0; top: 400px;
    text-align: center;
    color: var(--silver);
    font-family: "Pinyon Script", cursive;
    font-size: 38px; letter-spacing: 2px;
  }
</style>
</head>
<body>
  <main class="sheet">
    <section class="card card-front" aria-label="Card front">
      <div class="brand">
        <span class="brand-mark" aria-hidden="true"></span>
        <span class="brand-name">BRIXLEY ELECTRICAL</span>
      </div>
      <p class="brand-tagline">Professional cost effective solutions to all your electrical needs</p>
      <h1 class="holder-name">GAVIN PRESTWORTH</h1>
      <div class="name-rule"></div>
      <ul class="contact-list">
        <li>0417352940</li>
        <li>brixleyelectrical@quillnet.com.au</li>
        <li>lic no 81926 ac lic no l593721 abn 37216405813</li>
      </ul>
    </section>

    <section class="card card-back" aria-label="Card back">
      <div class="services-band">
        <h2 class="services-title">Services</h2>
        <p class="services-list">Real estate and commercial maintenance, New home and renovation rewires and upgrades, Split system air conditioning, Floor heat, Tv phone data, Smoke detectors, Lighting systems, builders welcome</p>
      </div>
      <p class="tagline">Powerful Solutions<br>For<br>Your Electrical Needs</p>
      <p class="thanks">Thank you</p>
    </section>
  </main>
</body>
</html>
```